Export Marketing company is looking for a web page design

Your projects should contain:

1. Header: Logo provided by us.
2. Top nav bar: offer, about us, experience, contact.
3. “Choose language” button.
4. Main section: panoramic picture (static, professional, modern).
5. Below section: 3 blocks (image+title+description), which represent our 3 main activities (titles):
• Market Research,
• Marketing Plans,
• Marketing Project.
6. ‘Contact us’ form – Message (text: “Write your message and give us details about your company and activities”), Email, SEND).
7. Page footer: (4 section: Contact, Social Media, Blog, Partners).
Updates

Hello!

I uploaded new file 'general_look', which is our idea how the page should generally look like.

BUT! it doesn't mean that your projects should look exactly like this project e.g.:
* titles Market Research, Marketing Plans, Marketing Project can be above these: Image 1,2,3.
* everything doesn't have to be in square and rectangle shape. You can try to manipulate with blocks and can add elipse elemnts or something similar.

We will appreciate your innovative ideas. Just wanted to give you general plan of the site and ilustrate all elements that we require.

Best Regards,
Teodor

IMPORTENT

Please remember that the main picture should be panoramic. Please do not close it in frame.

Target Market(s)

Small and middle sized companies, which would like to export their goods and services abroad and are interested in raising funds from Coastal Alliance to expand their activities. These are rather industrial companies with low level of innovativeness. Our mission is to build image of the client’s company and increase awareness of their products to improve their competitiveness and innovativeness.

Industry/Entity Type

It Company

Requirements
Must have
• 1. Create designs of main page and subpage.
2. Subpage: Logo, Header, language button, place for article, navigation menu on the right side - below it “contact us” button , footer on the bottom. (In this section we are looking mainly for the design of the header and navigation menu).
3. The whole design should be a series of horizontal blocks.
4. Your projects should be associated with features such as: Reliability, Security, Professionalism, Openness, Uniqueness.
5. The design should be simple, fresh, readable, easy to use and should create a feeling of high quality services.
6. Possibility to change the panoramic picture (separate layer in a graphic file).
7. All pictures and blocks should be static, no movements.
8. Style of the page should be compliant with the logo design, font: Swiss.
9. Designs that we like: http://www.brixomedia.pl/, http://www.zentrofalu.com/.
Should not have
• There shouldn’t be any distractions and not matching parts (whole design should be compact and easy to interpret and remember).

```html
<!DOCTYPE html>
<html lang="en">
<head>
<meta charset="utf-8">
<title>Tradeway Partners</title>
<link href="https://fonts.googleapis.com/css2?family=Arimo:wght@400;700&display=swap" rel="stylesheet">
<style>
  :root{
    --sky:#11a7d2;
    --sky-deep:#0d8fb6;
    --white:#ffffff;
    --mist:#e6eaee;
    --navy-text:#23307a;
    --ink:#3b3f45;
    --footer:#1f2a36;
    --footer-text:#d5dbe2;
    --line:#c9d0d7;
    --field:#f6f5f5;
    --field-border:#d4d6da;
    --caption:rgba(60,90,110,.78);
    --dot:#c9d3da;
    --dot-active:#4fc3ec;
  }
  *{box-sizing:border-box;margin:0;padding:0}
  html,body{width:860px;height:1200px;overflow:hidden;background:var(--white)}
  body{font-family:"Arimo",Arial,sans-serif;color:var(--ink)}
  .page{position:relative;width:860px;height:1200px;overflow:hidden}

  .band-top{position:absolute;left:0;top:0;width:860px;height:308px;background:var(--sky)}
  .band-white{position:absolute;left:0;top:308px;width:860px;height:117px;background:var(--white)}
  .band-mist{position:absolute;left:0;top:425px;width:860px;height:503px;background:var(--mist)}
  .band-footer{position:absolute;left:0;top:928px;width:860px;height:272px;background:var(--footer)}

  .brand{position:absolute;left:113px;top:38px;display:flex;align-items:center;gap:6px}
  .brand-mark{width:30px;height:30px;border-radius:50%;background:var(--sky-deep)}
  .brand-name{font-size:18px;font-weight:700;color:#1d3f7a;letter-spacing:-.3px}

  .lang{position:absolute;left:632px;top:27px;width:115px;height:18px;background:var(--white);border:1px solid #c7ccd1;font-size:8px;letter-spacing:.6px;display:flex;align-items:center;padding-left:6px;color:#333}
  .lang-flag{width:11px;height:7px;margin-left:6px;background:linear-gradient(#c9323a 50%,#fff 50%);background-size:100% 2px;position:relative}
  .lang-flag::before{content:"";position:absolute;left:0;top:0;width:5px;height:4px;background:#2b3f8c}
  .lang-arrow{position:absolute;right:0;top:0;width:16px;height:16px;background:#d9dde1;border-left:1px solid #b9bec4}
  .lang-arrow::after{content:"";position:absolute;left:4px;top:6px;border:4px solid transparent;border-top:5px solid #222}

  .nav{position:absolute;left:430px;top:78px;display:flex;font-size:9px;letter-spacing:1px;color:#104a63}
  .nav a{color:inherit;text-decoration:none}
  .nav .sep{margin:0 20px}

  .hero-shadow{position:absolute;left:125px;top:385px;width:610px;height:36px;border-radius:50%;background:radial-gradient(ellipse at center,rgba(0,0,0,.85) 0%,rgba(0,0,0,.4) 55%,rgba(0,0,0,0) 75%)}
  .hero{position:absolute;left:113px;top:122px;width:634px;height:270px;background:linear-gradient(100deg,#1b5f85 0%,#2f86ad 35%,#5aa8cc 65%,#a9d3ea 100%)}
  .hero-caption{position:absolute;left:0;bottom:0;width:100%;height:44px;background:var(--caption);color:#e9f2f7;font-size:9px;letter-spacing:1.1px;line-height:13px;padding:10px 24px}
  .hero-dots{position:absolute;right:26px;top:18px;display:flex;gap:4px}
  .hero-dots span{width:9px;height:9px;border-radius:50%;background:var(--dot)}
  .hero-dots span.on{background:var(--dot-active)}

  .service{position:absolute;top:460px;width:170px}
  .service-image{width:143px;height:90px;border:2px solid #fff;border-radius:3px}
  .service-title{margin-top:21px;font-size:12px;letter-spacing:1.3px;color:var(--navy-text);font-weight:400;text-align:center;width:143px}
  .service-text{margin-top:10px;font-size:8px;line-height:9.6px;color:#444;width:155px}
  .service-more{position:absolute;top:211px;left:0;font-size:8px;font-style:italic;color:#222}

  .divider{position:absolute;left:137px;top:711px;width:585px;height:1px;background:var(--line)}

  .contact-title{position:absolute;left:137px;top:737px;font-size:12px;letter-spacing:1.4px;color:var(--navy-text);font-weight:400}
  .field-label{position:absolute;top:767px;font-size:8px;font-weight:700;color:#333;letter-spacing:.4px}
  .field{position:absolute;background:var(--field);border:1px solid var(--field-border);font-size:8px;color:#8a8d92;padding:7px 9px;letter-spacing:.4px}
  .submit{position:absolute;left:554px;top:844px;width:59px;height:21px;background:#ece9e9;border:1px solid #c9c6c6;font-size:8px;font-weight:700;letter-spacing:1px;color:#333;display:flex;align-items:center;justify-content:center}

  .foot-head{position:absolute;top:946px;font-size:11px;letter-spacing:1.6px;color:var(--footer-text);font-weight:400}
  .foot-text{position:absolute;font-size:8px;line-height:10px;color:var(--footer-text);letter-spacing:.4px}
  .social-icon{position:absolute;left:289px;width:20px;height:20px;border-radius:3px}
  .partner-icon{position:absolute;left:585px;width:12px;height:12px}
  .blog-copy{position:absolute;left:438px;top:1015px;width:118px;font-size:7.5px;line-height:9.2px;color:var(--footer-text)}
  .foot-legal{position:absolute;top:1172px;font-size:8px;letter-spacing:.8px;color:var(--footer-text)}
</style>
</head>
<body>
<div class="page">
  <div class="band-top"></div>
  <div class="band-white"></div>
  <div class="band-mist"></div>
  <div class="band-footer"></div>

  <header>
    <div class="brand"><span class="brand-mark"></span><span class="brand-name">Tradeway Partners</span></div>
    <div class="lang">Select Language<span class="lang-flag"></span><span class="lang-arrow"></span></div>
    <nav class="nav">
      <a href="#">OFFER</a><span class="sep">|</span>
      <a href="#">ABOUT US</a><span class="sep">|</span>
      <a href="#">EXPERIENCE</a><span class="sep">|</span>
      <a href="#">CONTACT</a>
    </nav>
  </header>

  <div class="hero-shadow"></div>
  <section class="hero" role="img" aria-label="Panoramic photo of a glass globe on cubes against a blue cloudy sky">
    <div class="hero-caption">
      WE CREAT A INVATIVE WORKFORCE SOLUTION<br>THAT MAKE BUSINESS SUCCESS HUMANLY POSSIBLE
      <div class="hero-dots"><span></span><span></span><span></span><span class="on"></span></div>
    </div>
  </section>

  <section class="services">
    <article class="service" style="left:143px">
      <div class="service-image" role="img" aria-label="Photo of blue 3D bar and pie charts" style="background:linear-gradient(135deg,#1e3fa8,#4f8fe0 55%,#b9d9f5)"></div>
      <h2 class="service-title">MARKET RESEARCH</h2>
      <p class="service-text">Lorem Ipsum is simply dummy text of the printing and typesetting industry. Lorem Ipsum has beensheets containing Lorem Ipsum passages, and more recently with desktop publishing software like Quill Layout including versions of Lorem Ipsum.</p>
      <a class="service-more">Read more</a>
    </article>
    <article class="service" style="left:357px">
      <div class="service-image" role="img" aria-label="Photo of green street signs under a blue sky" style="background:linear-gradient(180deg,#3a78c4,#7fb2e2 60%,#dbe9f6)"></div>
      <h2 class="service-title">MARKET PLANS</h2>
      <p class="service-text">Lorem Ipsum is simply dummy text of the printing and typesetting industry. Lorem Ipsum has beensheets containing Lorem Ipsum passages, and more recently with desktop publishing software like Quill Layout including versions of Lorem Ipsum.</p>
      <a class="service-more">Read more</a>
    </article>
    <article class="service" style="left:574px">
      <div class="service-image" role="img" aria-label="Photo of two business people at a meeting table" style="background:linear-gradient(135deg,#8a6a52,#b99a80 50%,#3e3a3c)"></div>
      <h2 class="service-title">MARKET PROJECTS</h2>
      <p class="service-text">Lorem Ipsum is simply dummy text of the printing and typesetting industry. Lorem Ipsum has beensheets containing Lorem Ipsum passages, and more recently with desktop publishing software like Quill Layout including versions of Lorem Ipsum.</p>
      <a class="service-more">Read more</a>
    </article>
  </section>

  <div class="divider"></div>

  <section class="contact">
    <h2 class="contact-title">CONTACT US FOR QUICK SOLUTION:-</h2>
    <span class="field-label" style="left:138px">Message :</span>
    <span class="field-label" style="left:459px">Email Address :</span>
    <div class="field" style="left:138px;top:789px;width:263px;height:78px">Type your message here</div>
    <div class="field" style="left:459px;top:789px;width:263px;height:28px">info@tradewaymail.com</div>
    <div class="submit">SUBMIT</div>
  </section>

  <footer>
    <h3 class="foot-head" style="left:137px">CONTACT</h3>
    <h3 class="foot-head" style="left:289px">SOCIAL MEDIA</h3>
    <h3 class="foot-head" style="left:438px">BLOG</h3>
    <h3 class="foot-head" style="left:585px">PARTNER</h3>

    <p class="foot-text" style="left:139px;top:1040px;line-height:12px">Company contact<br>information goes here</p>

    <span class="social-icon" style="top:978px;background:#3b5b98"></span>
    <span class="foot-text" style="left:334px;top:983px">FACELINK</span>
    <span class="social-icon" style="top:1006px;background:#3aa3d4"></span>
    <span class="foot-text" style="left:334px;top:1011px">CHIRPLINE</span>
    <span class="social-icon" style="top:1034px;background:#ef8a25"></span>
    <span class="foot-text" style="left:334px;top:1039px">RSS FEED</span>
    <span class="social-icon" style="top:1062px;background:#4a6fb0"></span>
    <span class="foot-text" style="left:334px;top:1067px">NOTELY</span>
    <span class="social-icon" style="top:1090px;background:#3a3d42"></span>
    <span class="foot-text" style="left:334px;top:1095px">ORBIT +</span>

    <svg style="position:absolute;left:438px;top:978px" width="30" height="22" viewBox="0 0 30 22" aria-hidden="true">
      <path d="M3 8h5l14-7v20L8 14H3z" fill="#e8eef4"/>
      <rect x="5" y="14" width="4" height="7" fill="#e8eef4"/>
      <path d="M25 7q3 4 0 8" stroke="#e8eef4" stroke-width="1.5" fill="none"/>
    </svg>
    <p class="blog-copy">Lorem Ipsum is simply dummy text of the printing and typesetting industry. Lorem Ipsum has beensheets containing Lorem Ipsum passages, and more recently with desktop publishing software like Quill Layout including versions of Lorem Ipsum.</p>
    <span class="foot-text" style="left:534px;top:1101px;font-style:italic;text-decoration:underline">Name</span>

    <svg class="partner-icon" style="top:985px" viewBox="0 0 12 12" aria-hidden="true"><rect x=".5" y=".5" width="11" height="11" fill="none" stroke="#e8eef4"/><path d="M3 6h6M6.5 3.5 9 6 6.5 8.5" stroke="#e8eef4" stroke-width="1.4" fill="none"/></svg>
    <span class="foot-text" style="left:620px;top:986px">Partner Name</span>
    <svg class="partner-icon" style="top:1010px" viewBox="0 0 12 12" aria-hidden="true"><rect x=".5" y=".5" width="11" height="11" fill="none" stroke="#e8eef4"/><path d="M3 6h6M6.5 3.5 9 6 6.5 8.5" stroke="#e8eef4" stroke-width="1.4" fill="none"/></svg>
    <span class="foot-text" style="left:620px;top:1011px">Partner Name</span>
    <svg class="partner-icon" style="top:1035px" viewBox="0 0 12 12" aria-hidden="true"><rect x=".5" y=".5" width="11" height="11" fill="none" stroke="#e8eef4"/><path d="M3 6h6M6.5 3.5 9 6 6.5 8.5" stroke="#e8eef4" stroke-width="1.4" fill="none"/></svg>
    <span class="foot-text" style="left:620px;top:1036px">Partner Name</span>
    <svg class="partner-icon" style="top:1061px" viewBox="0 0 12 12" aria-hidden="true"><rect x=".5" y=".5" width="11" height="11" fill="none" stroke="#e8eef4"/><path d="M3 6h6M6.5 3.5 9 6 6.5 8.5" stroke="#e8eef4" stroke-width="1.4" fill="none"/></svg>
    <span class="foot-text" style="left:620px;top:1062px">Partner Name</span>
    <svg class="partner-icon" style="top:1086px" viewBox="0 0 12 12" aria-hidden="true"><rect x=".5" y=".5" width="11" height="11" fill="none" stroke="#e8eef4"/><path d="M3 6h6M6.5 3.5 9 6 6.5 8.5" stroke="#e8eef4" stroke-width="1.4" fill="none"/></svg>
    <span class="foot-text" style="left:620px;top:1087px">Partner Name</span>

    <span class="foot-legal" style="left:138px">Copyright 2012-13 inc all rights reserved</span>
    <span class="foot-legal" style="left:616px">Term&nbsp;&nbsp;&nbsp;&nbsp;|&nbsp;&nbsp;&nbsp;&nbsp;Privacy Policy</span>
  </footer>
</div>
</body>
</html>
```